Opening Specials Flyer for SmileHaven Dental

We require a flyer design for our promotions/special offers for our new opening of Dental Practice. Please make one page flyer with designs on front and back
Opening Specials must be eye catchy, with images
FRONT - OPENING SPECIALS
BACK - MAP and Introduce our NEW CLINIC
on Back - MUST SAY "FLIP BACK OF FLYER TO VIEW OPENING SPECIAL OFFERS"

Opening specials to our local residents of West Ryde

Colour Scheme: Green, grey, white
Celebrate the opening of our new clinic
Opening Specials for West Ryde Residents include:

1. NO GAP Checkup for the whole family
NO GAP - Checkup Clean Fluoride X-rays - (to eligible health fund members)
2. Dental Crowns at half price - Full Ceramic $900 (includes core and crown, root canal extra) (please use picture of ceramic crown attached) - must bring voucher/flyer
3. Power tooth Whitening (Corvel Glint)- $400 must bring voucher/flyer
1hr office in chair whitening, immediate whitening results
4. 20% off all General Dental Treatment (must bring flyer- please design this onto flyer)
5. Free Healthcover Dental for Kids (for those eligible under Junior Oral Care Program up to $1000) - please have healthcover logo
6. Free consultation for second opinion of treatment plans

Emergency dental care available after hours, please contact (02) 7395 2268

Offer valid until 31st May 2016
by appointment only
No Gap for eligible health fund members only
Address: Shop 7/51-53 Larkin Rd West Ryde 2114
Please have image of atlas view of this location

Behind the flyer (back) I would like to introduce our new clinic:
MUST INCLUDE - Flip behind for opening special offers!

SmileHaven Dental is your Local Family Dentist
Newly opened in March 2016, we aim to provide local residents with affordable dentistry with a gentle friendly approach. We are a child friendly practice and welcome you and your family to visit our new clinic.

www.smilehavenclinic.com.au
info@smilehavenclinic.com.au
(02) 7395 2268

Target Market(s)

Residents of West Ryde and Surrounding Suburbs
Children and Family

Industry/Entity Type

Dental Clinic

Colors
acd036
b2b2b2

Requirements
Must have
• (You may phrase as you please)
• Newly Opened Dental Clinic in West Ryde
• Special Offers until 31st May 2016
• Specials and clearly big font "NO GAP"
• Healthcover logo (colour) next to "Free Healthcover Dental for Kids
• MUST have SmileHaven Dental Logo
• Must inform that voucher must be brought in order to claim specials
• Must have address: Shop 7/51-53 Larkin Rd West Ryde 2114
• Must have Ph: (02) 7395 2268
Nice to have
• Image of dental crown - full ceramic (attached)
• Image of Corvel Glint Whitening
• Map of Shop 7/51-53 Larkin Rd West Ryde (Atlas View)
• Happy family picture

```html
<!DOCTYPE html>
<html lang="en">
<head>
<meta charset="utf-8">
<title>SmileHaven Dental – Opening Specials Flyer</title>
<link href="https://fonts.googleapis.com/css2?family=Jost:wght@400;500;600;700&family=Oswald:wght@300;400;500;700&display=swap" rel="stylesheet">
<style>
  :root{
    --green:#8cc63f;
    --green-dark:#6fae2a;
    --green-pale:#e4f0d5;
    --grey:#6d6e70;
    --grey-dark:#4a4b4d;
    --grey-light:#b2b2b2;
    --ink:#2b2b2b;
    --white:#ffffff;
    --stage:#2f2f31;
  }
  *{margin:0;padding:0;box-sizing:border-box}
  html,body{width:1200px;height:831px;overflow:hidden;background:var(--stage)}
  body{position:relative;font-family:"Jost",sans-serif;color:var(--ink)}
  .flyer{position:absolute;top:46px;width:528px;height:745px;background:var(--white);overflow:hidden}
  .flyer--front{left:49px}
  .flyer--back{left:624px}
  .flyer__art{position:absolute;inset:0}
  .flyer__footer{position:absolute;left:0;right:0;bottom:0;height:30px;background:var(--green);
    border-top:4px solid var(--grey);display:flex;align-items:center;color:var(--grey-dark);font-size:12.5px}
  .icon{width:14px;height:14px;display:inline-block;vertical-align:middle;margin-right:6px}

  /* front */
  .brand-badge{position:absolute;left:334px;top:263px;width:138px;height:138px;border-radius:50%;
    background:var(--white);border:6px solid var(--grey);display:flex;align-items:center;justify-content:center;
    text-align:center;font-weight:500;font-size:21px;line-height:1.1;color:var(--grey)}
  .celebrate-panel{position:absolute;left:28px;top:392px;width:253px;height:272px;background:var(--green-pale)}
  .celebrate{position:absolute;left:48px;top:412px;font-family:"Oswald",sans-serif;color:var(--ink);line-height:1}
  .celebrate__line{display:block;font-weight:400;font-size:50px;letter-spacing:.5px;margin-bottom:8px}
  .celebrate__line--small{font-size:44px}
  .celebrate__line--bold{font-weight:700;font-size:52px}
  .celebrate__line--green{font-weight:700;font-size:46px;color:var(--green)}
  .phone-ribbon{position:absolute;left:13px;top:660px;width:284px;height:40px;background:var(--grey-dark);
    color:var(--white);font-family:"Oswald",sans-serif;font-size:26px;display:flex;align-items:center;justify-content:center;gap:8px}
  .phone-ribbon .icon{width:24px;height:24px;margin:0}
  .promise{position:absolute;left:320px;top:424px;font-family:"Oswald",sans-serif;font-weight:400;font-size:33px;line-height:1.32;color:var(--ink)}
  .no-gap{position:absolute;left:320px;top:568px;font-family:"Oswald",sans-serif;font-weight:700;font-size:60px;line-height:1;color:var(--grey)}
  .no-gap__accent{color:var(--green)}
  .no-gap-caption{position:absolute;left:320px;top:640px;font-weight:600;line-height:1.15}
  .no-gap-caption__main{display:block;font-size:29px}
  .no-gap-caption__sub{display:block;font-size:20px}
  .flyer--front .flyer__footer{justify-content:center;gap:18px}

  /* back */
  .brand-mark{position:absolute;left:64px;top:70px;font-weight:500;font-size:22px;line-height:1.1;color:var(--grey)}
  .flip-note{position:absolute;left:64px;top:128px;width:200px;font-weight:600;font-size:11px;line-height:1.3;letter-spacing:.4px;color:var(--green-dark)}
  .portrait{position:absolute;left:345px;top:251px;width:126px;height:126px;border-radius:50%;
    border:6px solid var(--green);background:radial-gradient(circle at 50% 40%,#e8d3c6,#9c7a63)}
  .specials{position:absolute;left:34px;top:394px;width:240px;font-size:10.4px;line-height:1.3;color:var(--ink)}
  .specials__title{color:var(--green);font-weight:500;font-size:15.5px;line-height:1.3;margin-bottom:7px}
  .specials__item{margin-bottom:4px}
  .specials__tag{font-weight:600;font-size:12.5px}
  .specials__tag em{font-style:normal;color:var(--green)}
  .specials__big{font-weight:600;font-size:20px;color:var(--green-dark);line-height:1}
  .specials__big-sub{font-weight:600;font-size:12.5px;display:block;margin-bottom:4px}
  .intro{position:absolute;right:34px;top:402px;width:216px;text-align:right;font-size:12px;line-height:1.38}
  .intro__lead{font-weight:500;font-size:15px;text-align:left;margin-bottom:2px}
  .emergency{position:absolute;left:297px;top:560px;width:200px;font-weight:500;font-size:15px;line-height:1.2;color:var(--ink)}
  .emergency__contact{display:block;color:var(--green);font-family:"Oswald",sans-serif;font-weight:400;font-size:18px;margin-top:4px}
  .terms{position:absolute;right:34px;top:628px;width:210px;text-align:right;font-size:12px;line-height:1.3;color:var(--grey)}
  .terms__voucher{display:block;color:var(--green-dark);font-weight:600}
  .flyer--back .flyer__footer{padding-left:34px;gap:16px}
  .social{margin-left:auto;margin-right:34px;display:flex;gap:6px}
  .social__dot{width:16px;height:16px;border-radius:50%;background:var(--white)}
</style>
</head>
<body>

<section class="flyer flyer--front">
  <svg class="flyer__art" viewBox="0 0 528 745" width="528" height="745">
    <defs>
      <linearGradient id="familyTone" x1="0" y1="0" x2="0" y2="1">
        <stop offset="0" stop-color="#a9cf73"/>
        <stop offset=".6" stop-color="#7fae4f"/>
        <stop offset="1" stop-color="#5f8f37"/>
      </linearGradient>
    </defs>
    <rect role="img" aria-label="Photo of a smiling family of four lying on the grass in a park" x="0" y="0" width="528" height="380" fill="url(#familyTone)"/>
    <path d="M0,360 C130,318 260,330 380,300 C450,283 500,290 528,290 L528,745 L0,745 Z" fill="var(--white)"/>
    <path d="M0,338 C150,292 290,322 400,300 C460,288 500,286 528,284 L528,322 C420,340 300,356 160,392 C80,410 30,428 0,444 Z" fill="var(--grey)"/>
    <path d="M250,392 C340,372 440,318 528,278 L528,424 C450,420 360,398 250,392 Z" fill="var(--green)"/>
  </svg>

  <div class="brand-badge">SmileHaven<br>Dental</div>

  <div class="celebrate-panel"></div>
  <h1 class="celebrate">
    <span class="celebrate__line">CELEBRATE</span>
    <span class="celebrate__line celebrate__line--small">THE OPENING</span>
    <span class="celebrate__line celebrate__line--bold">OF OUR</span>
    <span class="celebrate__line celebrate__line--green">NEW CLINIC</span>
  </h1>

  <div class="phone-ribbon">
    <svg class="icon" viewBox="0 0 24 24"><circle cx="12" cy="12" r="10.5" fill="none" stroke="#fff" stroke-width="2"/><path d="M8.5 6.5l2 2-1.2 1.6c.7 1.6 2 2.9 3.6 3.6l1.6-1.2 2 2-1.5 1.8c-3.8-.6-7.3-4.1-7.9-7.9z" fill="#fff"/></svg>
    02 7395 2268
  </div>

  <p class="promise">Quality Dental<br>Care You Can<br>Trust</p>
  <p class="no-gap">NO <span class="no-gap__accent">GAP</span></p>
  <p class="no-gap-caption">
    <span class="no-gap-caption__main">Checkup For</span>
    <span class="no-gap-caption__sub">The Whole Family</span>
  </p>

  <footer class="flyer__footer">
    <span>
      <svg class="icon" viewBox="0 0 16 16"><circle cx="8" cy="8" r="6.5" fill="none" stroke="#4a4b4d" stroke-width="1.3"/><ellipse cx="8" cy="8" rx="3" ry="6.5" fill="none" stroke="#4a4b4d" stroke-width="1.1"/><path d="M1.5 8h13" stroke="#4a4b4d" stroke-width="1.1"/></svg>www.smilehavenclinic.com.au
    </span>
    <span>
      <svg class="icon" viewBox="0 0 16 16"><path d="M8 1.5a4.5 4.5 0 0 0-4.5 4.5c0 3.4 4.5 8.5 4.5 8.5s4.5-5.1 4.5-8.5A4.5 4.5 0 0 0 8 1.5z" fill="none" stroke="#4a4b4d" stroke-width="1.2"/><circle cx="8" cy="6" r="1.6" fill="#4a4b4d"/></svg>Shop 7/51-53 Larkin Rd West Ryde 2114
    </span>
  </footer>
</section>

<section class="flyer flyer--back">
  <svg class="flyer__art" viewBox="0 0 528 745" width="528" height="745">
    <defs>
      <linearGradient id="clinicTone" x1="0" y1="0" x2="1" y2="1">
        <stop offset="0" stop-color="#f1f3f2"/>
        <stop offset=".6" stop-color="#e3e6e4"/>
        <stop offset="1" stop-color="#d7dbd6"/>
      </linearGradient>
    </defs>
    <rect role="img" aria-label="Photo of a smiling young girl in a dental clinic holding a model of teeth with braces" x="0" y="0" width="528" height="340" fill="url(#clinicTone)"/>
    <path d="M0,318 C120,292 260,290 380,282 C450,278 500,282 528,284 L528,745 L0,745 Z" fill="var(--white)"/>
    <path d="M0,262 C110,250 250,270 360,270 C420,270 470,262 500,258 L500,286 C420,292 300,296 180,310 C100,320 40,340 0,360 Z" fill="var(--grey)"/>
    <path d="M220,348 C290,330 360,300 400,294 C460,286 500,270 528,240 L528,380 C460,378 330,352 220,348 Z" fill="var(--green)"/>
  </svg>

  <div class="brand-mark">SmileHaven<br>Dental</div>
  <p class="flip-note">FLIP BACK OF FLYER TO VIEW<br>OPENING SPECIAL OFFERS</p>
  <div class="portrait" role="img" aria-label="Portrait photo of a smiling young woman"></div>

  <div class="specials">
    <h2 class="specials__title">Opening Specials for West Ryde Residents include:</h2>
    <p class="specials__item"><span class="specials__tag">1. NO <em>GAP</em></span> Checkup for the whole family<br><span class="specials__tag">NO <em>GAP</em></span> - Checkup Clean Fluoride X-rays<br>&nbsp;- (to eligible health fund members)</p>
    <p class="specials__item"><strong>2.</strong> Dental Crowns at half price - Full Ceramic $900 (includes core and crown, root canal extra) or <span class="specials__tag">NO <em>GAP</em></span> if Crown is covered by health insurance</p>
    <p class="specials__item"><strong>3.</strong> Power tooth Whitening (Corvel Glint) - $400</p>
    <p class="specials__big">4. 20% OFF</p>
    <span class="specials__big-sub">ALL GENERAL DENTAL TREATMENT</span>
    <p class="specials__item"><strong>5.</strong> Free Healthcover Dental for Kids (for those eligible under Junior Oral Care Program up to $1000)</p>
    <p class="specials__item"><strong>6.</strong> Free consultation for second opinion of treatment plans</p>
  </div>

  <div class="intro">
    <p class="intro__lead">SmileHaven Dental is your</p>
    <p>Local Family Dentist Newly opened in March 2016, we aim to provide local residents with affordable dentistry with a gentle friendly approach.<br>We are a child friendly practice and welcome you and your family to visit our new clinic.</p>
  </div>

  <p class="emergency">EMERGENCY DENTAL CARE AVAILABLE AFTER HOURS
    <span class="emergency__contact">PLEASE CONTACT 7395 2268</span>
  </p>

  <p class="terms">Offer valid until 1st May 2016<br>by appointment only<br>No Gap for eligible health<br>fund members only
    <span class="terms__voucher">Bring this flyer to claim specials</span>
  </p>

  <footer class="flyer__footer">
    <span>
      <svg class="icon" viewBox="0 0 16 16"><rect x="1.5" y="3.5" width="13" height="9" fill="none" stroke="#4a4b4d" stroke-width="1.2"/><path d="M1.5 3.5l6.5 5 6.5-5" fill="none" stroke="#4a4b4d" stroke-width="1.2"/></svg>info@smilehavenclinic.com.au
    </span>
    <span>
      <svg class="icon" viewBox="0 0 24 24"><circle cx="12" cy="12" r="10.5" fill="none" stroke="#4a4b4d" stroke-width="2"/><path d="M8.5 6.5l2 2-1.2 1.6c.7 1.6 2 2.9 3.6 3.6l1.6-1.2 2 2-1.5 1.8c-3.8-.6-7.3-4.1-7.9-7.9z" fill="#4a4b4d"/></svg>02 7395 2268
    </span>
    <span class="social"><span class="social__dot"></span><span class="social__dot"></span><span class="social__dot"></span></span>
  </footer>
</section>

</body>
</html>
```